Best Seller Cover Design for Inspirational Non-Fiction, Self-Help Book

I've been working diligently on a book title "Quietly Charted Harbor" that will be pivotal for my coaching business. We're heavily investing in marketing and public relations for this and would love it to be a best seller (every other's dream). I need an amazing book cover design that is eye-catching, description, creative, interesting, and compelling, Can you work your magic?I've attached a detailed description along with the content for the back cover. Please let me know if all the content does not fit and I'm happy to reduce it. I need a cover that sells and speaks to the description, whatever you think that will be best. Book DetailsTitle: Self-Defined SuccessSubtitle: Spoiler Alert: You Already Have Everything It TakesAuthor: Ngan H. NguyenSpecifics:- The book will be 5.5" by 8.5" and 216 pages (may change slightly and we can update the spine in final revisions). - Paperback and leave space for a bar code- Will need the raw files so this can be redesigned into hardcover down the line- Bookvale book cover upload ready- Final file will also need the front cover only for e-book version- Add profile headshot (attached) to back-cover if space permits.I do not have a clear vision of what will be best for this cover but I really like the evocative style of Oswin Tarkell Plentiful book. Thank you!

Target Market(s)

Professionals in transition, aspiring or new entrepreneurs, change-makers.

Font styles to use
Serif
Script

Colors

Designer to choose colors to be used in the design.

Requirements
Must have
• Traditional but with elements that make it interesting and provocative since it is speaking to a twist on a topic that has been well talked about, success.

```html
<!DOCTYPE html>
<html lang="en">
<head>
<meta charset="utf-8">
<title>Quietly Charted Harbor — Cover Wrap</title>
<link rel="stylesheet" href="https://fonts.googleapis.com/css2?family=Didact+Gothic&family=EB+Garamond:ital,wght@0,400;0,500;1,400&family=Oswald:wght@600&family=Roboto+Condensed:wght@700&display=swap">
<style>
  :root {
    --page-bg: #e4e4e2;
    --cover-navy: #1b2330;
    --cover-navy-deep: #121822;
    --cover-slate: #2a3444;
    --accent-orange: #f7941d;
    --band-orange: #f9a640;
    --text-light: #f2f2f2;
    --text-soft: #dcdfe4;
    --barcode-white: #ffffff;
  }
  * { box-sizing: border-box; margin: 0; padding: 0; }
  html, body {
    width: 1200px; height: 800px; overflow: hidden;
    background: var(--page-bg);
  }
  .cover-wrap {
    position: absolute; left: 108px; top: 40px;
    width: 984px; height: 720px;
    display: flex;
    box-shadow: 0 10px 30px rgba(0,0,0,0.25);
  }

  /* Back cover */
  .back-cover {
    position: relative; width: 466px; height: 720px;
    background: linear-gradient(160deg, var(--cover-navy) 0%, var(--cover-navy-deep) 100%);
    color: var(--text-light);
    font-family: "Didact Gothic", sans-serif;
    padding: 36px 30px 0 40px;
  }
  .back-headline {
    font-family: "Didact Gothic", sans-serif;
    color: var(--accent-orange);
    font-size: 19px; line-height: 1.2;
    text-align: center; margin-bottom: 16px; padding-left: 10px;
  }
  .back-blurb p {
    font-size: 11.4px; line-height: 1.24;
    color: var(--text-soft);
    text-align: justify; margin-bottom: 8px;
  }
  .author-bio {
    margin-top: 22px;
    font-size: 11.4px; line-height: 1.26;
    color: var(--text-soft);
    text-align: justify;
  }
  .author-headshot {
    float: left; width: 94px; height: 104px;
    margin: 2px 8px 4px 0;
    background: linear-gradient(180deg, #4b5a66 0%, #3a2e2a 60%, #1e1a18 100%);
  }
  .author-bio strong {
    font-family: "Roboto Condensed", sans-serif;
    font-style: italic; font-weight: 700; color: var(--text-light);
  }
  .barcode-space {
    position: absolute; right: 24px; bottom: 48px;
    width: 108px; height: 80px;
    background: var(--barcode-white);
    display: flex; align-items: center; justify-content: center;
    font-family: "Didact Gothic", sans-serif;
    font-size: 18px; color: #111;
  }

  /* Spine */
  .spine {
    width: 52px; height: 720px;
    background: linear-gradient(90deg, var(--cover-navy-deep), var(--cover-slate) 50%, var(--cover-navy-deep));
    display: flex; flex-direction: column; align-items: center;
    padding: 28px 0;
    writing-mode: vertical-rl;
  }
  .spine-title {
    font-family: "Roboto Condensed", sans-serif; font-weight: 700;
    font-size: 22px; letter-spacing: 0.5px; color: var(--text-light);
    white-space: nowrap;
  }
  .spine-author {
    margin-top: auto;
    font-family: "EB Garamond", serif; font-size: 15px;
    letter-spacing: 0.5px; color: var(--text-light);
    white-space: nowrap;
  }

  /* Front cover */
  .front-cover {
    position: relative; width: 466px; height: 720px; overflow: hidden;
    background: var(--cover-navy);
  }
  .front-artwork {
    position: absolute; inset: 0;
    background:
      radial-gradient(ellipse 40% 45% at 48% 50%, rgba(214,184,118,0.55), transparent 70%),
      radial-gradient(ellipse 55% 18% at 50% 72%, rgba(210,140,110,0.55), transparent 75%),
      linear-gradient(180deg, #26303f 0%, var(--cover-navy) 55%, var(--cover-navy-deep) 100%);
  }
  .subtitle-band {
    position: absolute; left: -10px; top: 40px;
    width: 500px; height: 30px;
    background: var(--band-orange);
    transform: rotate(-3.2deg);
    display: flex; align-items: center; justify-content: center;
    font-family: "EB Garamond", serif;
    font-size: 15px; color: var(--text-light);
  }
  .front-title {
    position: absolute; left: 0; right: 0; top: 100px;
    text-align: center; line-height: 0.95;
  }
  .title-top {
    display: block;
    font-family: "Oswald", sans-serif; font-weight: 600;
    font-size: 34px; color: var(--text-light);
  }
  .title-main {
    display: block;
    font-family: "Roboto Condensed", sans-serif; font-weight: 700;
    font-size: 74px; letter-spacing: 1px; color: var(--accent-orange);
  }
  .front-author {
    position: absolute; left: 0; right: 0; bottom: 44px;
    text-align: center;
    font-family: "EB Garamond", serif; font-weight: 500;
    font-size: 25px; letter-spacing: 1px; color: var(--text-light);
  }
</style>
</head>
<body>
  <main class="cover-wrap">
    <section class="back-cover">
      <h2 class="back-headline">When all is said and done,<br>what will matter to you most?</h2>
      <div class="back-blurb">
        <p>Following someone else’s path or society’s definition of “success” doesn’t often lead to personal fulfillment. At the end of the day, we genuinely want to succeed—not live a life defined by others.</p>
        <p>You can achieve anything you desire, and when you aim high for your spark of passion you will succeed. Passion is what awakens the heart, fires the soul, and fills the spirit. It is passion that energizes and sparks the pull forward through all barriers, uncertainty, and challenges.</p>
        <p>On this journey, we are asked to turn inward and search for the invisible, the hidden, and the sacred possibilities in order to claim what is ours in truth. We will then fill that shell with a desire that will ignite its creation.</p>
        <p>May this book serve as your guide on how to evoke this clarity and desire for your most authentic path enabling you to create a vision for your future that will bring you the ultimate sense of fulfillment. In addition, this book will show you the steps to navigate the path forward toward this new dream giving you the opportunity to awaken innate abilities you didn’t know you had that will open the door to success.</p>
      </div>
      <div class="author-bio">
        <div class="author-headshot" role="img" aria-label="Author headshot photograph"></div>
        <p><strong>Rilka T. Varsome</strong> has built her platform of a vision-driven life after 10 years of experience working as a business strategy advisor in Ledgerline 500 companies and at Harlow &amp; Brindle. Combining her advisory experience with her passion for spiritual principles of success, she now empowers entrepreneurs, change-makers, and leaders to step into their truth and bring their unique vision to life. Enabling them to change their lives, revolutionize their work, create greater impact in the world.</p>
      </div>
      <div class="barcode-space">Bar code</div>
    </section>

    <aside class="spine">
      <span class="spine-title">QUIETLY CHARTED HARBOR</span>
      <span class="spine-author">RILKA T. VARSOME</span>
    </aside>

    <section class="front-cover">
      <div class="front-artwork" role="img" aria-label="Photograph of a man in a dark suit holding a gold trophy in cupped hands"></div>
      <div class="subtitle-band">Fair Warning: The Map Was Folded In Your Pocket</div>
      <h1 class="front-title">
        <span class="title-top">QUIETLY CHARTED</span>
        <span class="title-main">HARBOR</span>
      </h1>
      <p class="front-author">RILKA T. VARSOME</p>
    </section>
  </main>
</body>
</html>
```